New Wordpress Design Project - Australian native plant nursery

I'm Seeking a wordpress website with landing page with contact details and social links, that page will link to another 4 pages. I'm happy to just add in the information once the template is set up (draft text provided on word doc).
Needing pages of information pages for:
- Nursery, what we carry and that we provide garden design services, pictures of plants and gardens
- Native flowers & what we provide, flower arrangements for weddings, special occasions, pictures
- Giftwear short blurb that we carry local artisan giftwear, pictures
- about us with history of the nursery & pictures
* Also wanting a link for e-gift cards. The link will go to an external page (square) so I don’t need to set up the website for purchases.
Social media links
Social links
https://www.facebook.com/TheBrambleHollow
https://www.instagram.com/thebramblehollownursery

Two local native nursery websites that I like the style of:
https://www.harbourfernplantnursery.com.au/
https://www.belmaro.com.au/

I'm using two versions of our logo, we have the smaller circle and then the other logo which is stretched out. We have used the second design for our signs at the nursery, I've asked the sign guy for a copy of the design as I don't currently have one. I have vector files of the other design.

We have wordpress set up with elemantor and hosting with godaddy, I can send you the logon details once design is confirmed.

Target Market(s)

Anyone who likes gardening, we have a pretty even spread of customers across male/female and all ages

Industry/Entity Type

Garden centre with native plants, flowers and giftwear

Coding

Coded - Design and coding required

Colors
0054AA
0677BA
7BADD7
CADEEF
E8F1F8
0094D4
00A9DD
6FCCEA
C7EBF8
E9F6FB
00AB8E
00BBA5
67D7C9
C6EFE9
E9F9F6

Requirements
Must have
• Organic/modern/minimalist design
Nice to have
• Blue/white/green, flannel flowers as per logo

```html
<!DOCTYPE html>
<html lang="en">
<head>
<meta charset="utf-8">
<title>The Bramble Hollow – Native Plant Nursery</title>
<link href="https://fonts.googleapis.com/css2?family=Bellefair&family=Jost:wght@400;500;600&display=swap" rel="stylesheet">
<style>
:root{
  --green:#0b8068;
  --navy:#1d4b69;
  --ink:#1b2a38;
  --muted:#5d6874;
  --mist:#eef0f3;
  --footer:#101f2d;
  --field:#2b4862;
  --white:#ffffff;
}
*{box-sizing:border-box;margin:0;padding:0}
html,body{width:1200px;height:5286px;overflow:hidden}
body{position:relative;background:var(--white);font-family:"Jost",sans-serif;color:var(--ink)}
a{color:inherit;text-decoration:none}
.abs{position:absolute}
.serif{font-family:"Bellefair",serif;font-weight:400}
.title{font-size:60px;line-height:68px;color:var(--ink);white-space:nowrap}
.body-copy{font-size:12.5px;line-height:27px;color:var(--muted)}
.label{font-size:17px;font-weight:500;letter-spacing:.5px;text-transform:uppercase}
.read-more{display:flex;align-items:center;height:42px;padding-left:30px;border-left:3px solid var(--green);font-size:15px;font-weight:600;letter-spacing:2px;color:var(--ink)}
.photo{position:absolute}
.arc{position:absolute;border:1.5px solid #9aa6b0;border-radius:50%;border-right-color:transparent;border-top-color:transparent;transform:rotate(45deg)}

/* header */
.brand{left:85px;top:22px;display:flex;align-items:center;gap:12px}
.brand-mark{width:44px;height:44px;border:1.5px solid var(--navy);border-radius:50%}
.brand-name{font-family:"Bellefair",serif;font-size:30px;color:var(--navy);line-height:1;white-space:nowrap}
.nav{left:402px;top:48px;display:flex;gap:30px;font-size:14.5px;color:#3b4956}
.nav a:first-child{color:var(--navy)}
.nav-ring{left:368px;top:26px;width:52px;height:52px}
.gift-btn{left:965px;top:35px;width:148px;height:51px;background:var(--green);color:#fff;font-size:14px;font-weight:600;display:flex;align-items:center;justify-content:center;border-radius:2px}

/* flowers */
.flowers{top:1268px;left:0;width:1200px;height:989px;background:var(--mist)}
.slide-tab{position:absolute;background:var(--green);color:#fff;font-size:15px;font-weight:600;clip-path:polygon(0 0,82% 0,100% 16%,100% 100%,0 100%)}
.slide-tab .num{position:absolute;left:54px;top:54px}
.slide-tab .bar{position:absolute;left:54px;top:84px;width:30px;height:4px;background:rgba(255,255,255,.5)}
.slide-tab .bar::before{content:"";position:absolute;left:0;top:0;width:12px;height:4px;background:#fff}
.arrows{display:flex;gap:20px}
.arrow{width:50px;height:50px;border-radius:50%;border:1.5px solid #7a8591;display:flex;align-items:center;justify-content:center}
.arrow.next{border-color:var(--green);border-width:2px}

/* history */
.history{top:3153px;left:0;width:1200px;height:984px;background:var(--navy)}
.plus-tab{position:absolute;width:94px;height:100px;background:var(--green);clip-path:polygon(0 0,75% 0,100% 22%,100% 100%,0 100%);display:flex;align-items:center;justify-content:center}

/* footer */
.footer{top:4733px;left:0;width:1200px;height:553px;background:var(--footer);color:#fff}
.f-label{font-size:12.5px;letter-spacing:.5px;text-transform:uppercase;color:#c5ccd3}
.f-value{font-size:15.5px;font-weight:500;line-height:30px;color:#fff}
.social{width:40px;height:40px;border:1.5px solid #d0d6dc;border-radius:50%;display:block}
</style>
</head>
<body>

<header>
  <a class="abs brand" href="#"><span class="brand-mark"></span><span class="brand-name">The Bramble Hollow</span></a>
  <svg class="abs nav-ring" viewBox="0 0 52 52" aria-hidden="true"><path d="M26 50A24 24 0 0 1 8 10" fill="none" stroke="#8796a3" stroke-width="1.2"/></svg>
  <nav class="abs nav"><a href="#">Nursery</a><a href="#">What we provide</a><a href="#">Giftwear</a><a href="#">About us</a></nav>
  <a class="abs gift-btn" href="#">e-gift cards</a>
</header>

<section class="hero">
  <div class="arc" style="left:170px;top:210px;width:330px;height:330px;border-color:#e4e7ea;border-right-color:transparent;border-top-color:transparent"></div>
  <h1 class="abs serif title" style="left:85px;top:275px;font-size:61px;line-height:74px">Welcome to our<br>native plant nursery<br>information page</h1>
  <div class="abs body-copy" style="left:698px;top:272px;width:420px">
    <p>At our nursery, we provide native plants that thrive in their local environment. Native plants are essential for preserving biodiversity, and they support pollinators and other wildlife while reducing human impact on the environment.</p>
    <p style="margin-top:6px">At our nursery, we offer a wide selection of native plants that are suitable for a variety of different environments,</p>
  </div>
  <a class="abs read-more" href="#" style="left:700px;top:477px">READ MORE</a>
  <div class="photo" role="img" aria-label="Close-up of a native flower bouquet with banksia, wattle and purple blooms" style="left:0;top:715px;width:1200px;height:553px;background:linear-gradient(120deg,#7d9a4a 0%,#b89ac0 22%,#9aa75a 40%,#5f7d3a 60%,#8a86c8 78%,#c79dba 100%)"></div>
  <div class="abs" style="left:925px;top:1218px;width:275px;height:97px;background:#fff;display:flex;align-items:center;padding-left:30px;gap:22px;font-size:17px;color:var(--ink)">
    Scrolldown
    <svg width="46" height="46" viewBox="0 0 46 46" aria-hidden="true"><circle cx="23" cy="23" r="21" fill="none" stroke="var(--navy)" stroke-width="2"/><path d="M16 20l7 7 7-7" fill="none" stroke="var(--navy)" stroke-width="2"/></svg>
  </div>
</section>

<section class="abs flowers">
  <div class="arc" style="left:60px;top:78px;width:90px;height:90px"></div>
  <p class="abs label" style="left:97px;top:122px;color:var(--green)">Flowers</p>
  <h2 class="abs serif title" style="left:100px;top:150px">At the nursery,<br>we specialize</h2>
  <p class="abs body-copy" style="left:580px;top:122px;width:530px">In creating unique arrangements using locally sourced native Australian flowers. Our team of experienced florists are passionate about showcasing the beauty of our country's flora and fauna through unique and beautiful bespoke floral designs. Our native flower arrangements are perfect for any occasion</p>
  <a class="abs read-more" href="#" style="left:578px;top:262px">READ MORE</a>

  <div class="photo" role="img" aria-label="Potted native plants on garden soil" style="left:0;top:359px;width:122px;height:410px;background:linear-gradient(160deg,#6f7a4c,#8c7660 60%,#5a4a3c)"></div>
  <div class="photo" role="img" aria-label="Pink kangaroo paw flowers close up" style="left:213px;top:359px;width:772px;height:410px;background:radial-gradient(ellipse at 45% 45%,#e892a8 0%,#d77d96 25%,#6b8a44 55%,#2f4a22 100%)"></div>
  <div class="photo" role="img" aria-label="Red and cream flowering gum blossoms" style="left:1076px;top:359px;width:124px;height:410px;background:linear-gradient(170deg,#b8485a,#e6c3a8 50%,#c25a5e)"></div>
  <div class="slide-tab" style="left:180px;top:600px;width:145px;height:169px"><span class="num">01</span><span class="bar"></span></div>
  <div class="slide-tab" style="left:1034px;top:600px;width:146px;height:169px"><span class="num">02</span><span class="bar"></span></div>
  <div class="abs arrows" style="left:539px;top:804px">
    <a class="arrow" href="#" aria-label="Previous"><svg width="10" height="12" viewBox="0 0 10 12"><path d="M9 0v12L0 6z" fill="var(--ink)"/></svg></a>
    <a class="arrow next" href="#" aria-label="Next"><svg width="10" height="12" viewBox="0 0 10 12"><path d="M1 0v12l9-6z" fill="var(--ink)"/></svg></a>
  </div>
</section>

<section class="giftwear">
  <div class="arc" style="left:105px;top:2382px;width:120px;height:120px"></div>
  <p class="abs label" style="left:0;width:1210px;top:2380px;text-align:center;color:var(--navy)">Giftwear</p>
  <h2 class="abs serif title" style="left:0;width:1200px;top:2407px;text-align:center;font-size:60px">We are proud to offer a wide range<br>of unique and high-quality gifts</h2>
  <div class="abs" style="left:598px;top:2583px;width:3px;height:36px;background:var(--green)"></div>
  <div class="photo" role="img" aria-label="Purple fan flowers in a nursery pot with a plant label" style="left:85px;top:2698px;width:465px;height:325px;clip-path:polygon(0 0,90% 0,100% 13%,100% 100%,0 100%);background:linear-gradient(135deg,#4c6b34,#9b8fd4 45%,#6a7f3e 75%,#2e4622)"></div>
  <h3 class="abs" style="left:613px;top:2692px;font-size:32px;line-height:46px;font-weight:500;color:var(--ink);white-space:nowrap">That celebrate the natural<br>beauty of Australia's native<br>flora and fauna</h3>
  <div class="abs body-copy" style="left:613px;top:2860px;width:500px;font-size:12.5px;line-height:22px">
    <p>From beautifully scented candles to stunning artworks, our gift selection is sure to please. Our giftware collection features a range of products that have been designed and crafted by local artisans and small businesses. We believe in supporting our community and showcasing the amazing talent and creativity that can be found here in Australia.</p>
    <p style="margin-top:8px">In addition to our locally made products, we also stock gifts from well-known brands that share our passion for nature and sustainability.</p>
  </div>
</section>

<section class="abs history">
  <div class="arc" style="left:82px;top:82px;width:90px;height:90px;border-color:#c6d0d9;border-right-color:transparent;border-top-color:transparent"></div>
  <p class="abs label" style="left:110px;top:122px;color:#fff">History</p>
  <h2 class="abs serif title" style="left:115px;top:150px;color:#fff">The Bramble<br>Hollow business</h2>
  <p class="abs" style="left:640px;top:170px;width:480px;font-size:12.5px;line-height:27px;color:#fff">That has been providing plants, flowers and native giftware to the Central Coast and surrounding areas since 2001. Over this time, we have established a strong connection with the community and provided expert native advice.</p>

  <div class="photo" role="img" aria-label="White flowering native shrub" style="left:0;top:345px;width:135px;height:417px;background:linear-gradient(150deg,#3f5a2c,#d9dcc8 45%,#5b7038)"></div>
  <div class="photo" role="img" aria-label="Mixed native bouquet with banksia and grasses" style="left:193px;top:345px;width:377px;height:417px;background:linear-gradient(160deg,#b86a54,#7a8f44 35%,#c9b57a 55%,#8b86c6 80%,#4f6a36)"></div>
  <div class="photo" role="img" aria-label="Floral arrangement in a rustic wooden vessel" style="left:630px;top:345px;width:376px;height:417px;background:linear-gradient(165deg,#6b4e34,#c2b03e 30%,#8a4a5c 60%,#9a9a98 85%)"></div>
  <div class="photo" role="img" aria-label="Green native foliage" style="left:1064px;top:345px;width:136px;height:417px;background:linear-gradient(160deg,#2f4a24,#6d8a3e 55%,#3c5a2a)"></div>
  <div class="plus-tab" style="left:193px;top:662px"><svg width="26" height="26" viewBox="0 0 26 26"><path d="M13 2v22M2 13h22" stroke="#fff" stroke-width="1.6"/></svg></div>
  <div class="plus-tab" style="left:630px;top:662px"><svg width="26" height="26" viewBox="0 0 26 26"><path d="M13 2v22M2 13h22" stroke="#fff" stroke-width="1.6"/></svg></div>
  <div class="plus-tab" style="left:1064px;top:662px"><svg width="26" height="26" viewBox="0 0 26 26"><path d="M13 2v22M2 13h22" stroke="#fff" stroke-width="1.6"/></svg></div>
  <div class="abs arrows" style="left:539px;top:805px">
    <a class="arrow" href="#" aria-label="Previous" style="border-color:#fff"><svg width="10" height="12" viewBox="0 0 10 12"><path d="M9 0v12L0 6z" fill="#fff"/></svg></a>
    <a class="arrow next" href="#" aria-label="Next"><svg width="10" height="12" viewBox="0 0 10 12"><path d="M1 0v12l9-6z" fill="#fff"/></svg></a>
  </div>
</section>

<section class="nursery-now">
  <div class="arc" style="left:212px;top:4262px;width:140px;height:140px"></div>
  <p class="abs label" style="left:0;width:1210px;top:4262px;text-align:center;color:var(--navy)">The nursery now</p>
  <h2 class="abs serif title" style="left:0;width:1200px;top:4290px;text-align:center;font-size:62px">Since then concentrating<br>strictly on native only</h2>
  <div class="abs" style="left:598px;top:4484px;width:3px;height:36px;background:var(--green)"></div>
  <div class="abs body-copy" style="left:190px;top:4543px;width:820px;text-align:center;font-size:12.5px;line-height:26px">
    <p>The business was originally established by Edith and Marlene, ** later departed and Carys and Delia.</p>
    <p style="margin-top:4px">Edith Marsh has been in the native plant industry for most of her life. She has been involved in the propagation, wholesale, retail, floral design and promotion of native plants.</p>
  </div>
</section>

<footer class="abs footer">
  <p class="abs f-label" style="left:85px;top:142px">Newsletter</p>
  <p class="abs f-value" style="left:85px;top:168px;width:340px;font-size:16.5px;line-height:35px">SUBSCRIBE OUR NEWSLETTER FOR UPDATE</p>
  <div class="abs" style="left:85px;top:259px;width:237px;height:45px;background:var(--field);display:flex;align-items:center;padding-left:22px;font-size:13px">Email Address</div>
  <a class="abs" href="#" style="left:322px;top:259px;width:112px;height:45px;background:var(--green);display:flex;align-items:center;justify-content:center;font-size:14.5px;font-weight:600">Subscribe</a>

  <p class="abs f-label" style="left:525px;top:154px">Call us</p>
  <p class="abs f-value" style="left:525px;top:192px">+61 2 4000 1287</p>

  <p class="abs f-label" style="left:795px;top:154px">Visit us</p>
  <p class="abs f-value" style="left:795px;top:182px;font-size:14.5px">128 RIDGELINE ROAD,<br>TARRIN, NSW, AUSTRALIA,<br>NEW SOUTH WALES</p>

  <p class="abs f-label" style="left:525px;top:296px">Follow us</p>
  <div class="abs" style="left:528px;top:330px;display:flex;gap:16px">
    <a class="social" href="#" aria-label="Social profile one"></a>
    <a class="social" href="#" aria-label="Social profile two"></a>
  </div>

  <p class="abs f-label" style="left:798px;top:296px">Email us</p>
  <p class="abs f-value" style="left:798px;top:335px;font-size:14.5px">INFO@THEBRAMBLEHOLLOW.COM</p>

  <a class="abs brand" href="#" style="left:90px;top:402px"><span class="brand-mark" style="border-color:#fff"></span><span class="brand-name" style="color:#fff">The Bramble Hollow</span></a>

  <p class="abs" style="left:525px;top:497px;font-size:12px;color:#6f7d8a">© 2023 <span style="color:#fff">The Bramble Hollow</span> All right reserved</p>
  <p class="abs" style="left:957px;top:497px;font-size:12px;color:#6f7d8a">May 29, 2023. Layout_4</p>
</footer>

</body>
</html>
```